WordPress Site That Reviews Footwear

We need a wordpress web design for an affiliate site called TarnWisp. We review and do roundups on footwear products. The final design should be clean and mobile friendly. The site should be built with Gutenberg page builder. We like the design of https://petalharvin.com/.

Target Market(s)

USA

Industry/Entity Type

Footwear

Logo Text

TarnWisp

Number of Pages Required

4 page

Font styles to use
Serif
Sans Serif

Requirements
Must have
• Wordpress site
Blog post
Page
Categories
Homepage

```html
<!DOCTYPE html>
<html lang="en">
<head>
<meta charset="utf-8">
<title>TarnWisp — Outdoor Footwear Reviews</title>
<link href="https://fonts.googleapis.com/css2?family=Barlow+Condensed:wght@600;700&family=Jost:wght@400;500&display=swap" rel="stylesheet">
<style>
:root{
  --teal:#08576a;
  --orange:#ef7a3b;
  --ink:#1c2326;
  --body:#2c3438;
  --bg:#eaf0f2;
  --white:#ffffff;
  --card-grey:#eef0f1;
}
*{box-sizing:border-box;margin:0;padding:0}
html,body{width:1200px;height:2465px;overflow:hidden}
body{font-family:"Jost",sans-serif;color:var(--body);background:var(--bg)}
.page{position:relative;width:1200px;height:2465px;overflow:hidden;
  background:linear-gradient(180deg,#e6edf0 0,#f7f9fa 420px,#fff 520px,#fff 1950px,#e9eff2 2150px,#dfe7eb 2465px)}
.abs{position:absolute}
.display{font-family:"Barlow Condensed",sans-serif;font-weight:700;color:var(--ink);text-transform:uppercase;line-height:1}
.kicker{font-family:"Barlow Condensed",sans-serif;font-weight:700;letter-spacing:3px;text-transform:uppercase;font-size:14px}
.text{font-size:13.5px;line-height:19px}

/* header */
.site-header{left:0;top:0;width:1200px;height:80px;background:var(--white)}
.nav{top:35px;display:flex;gap:22px;font-family:"Barlow Condensed",sans-serif;font-weight:700;font-size:12.5px;letter-spacing:1.3px;color:var(--ink);text-transform:uppercase}
.nav span.drop::after{content:"";display:inline-block;width:4px;height:4px;border-right:1.5px solid var(--ink);border-bottom:1.5px solid var(--ink);transform:rotate(45deg);margin:0 0 3px 5px}
.brand{font-family:"Barlow Condensed",sans-serif;font-weight:700;font-size:32px;color:var(--ink);letter-spacing:.5px;text-transform:uppercase}
.social-dots{top:36px;left:958px;display:flex;gap:23px}
.social-dots i{width:13px;height:13px;border-radius:3px;background:var(--ink);display:block}

/* hero */
.hero-title{left:158px;top:183px;font-size:40px;line-height:38px}
.arrow-link{display:inline-flex;align-items:center;gap:8px;padding-bottom:4px;border-bottom:2px solid currentColor}
.arrow{width:12px;height:10px}
.slide{border-radius:8px;overflow:hidden}
.slide-label{font-family:"Barlow Condensed",sans-serif;font-weight:700;text-transform:uppercase;z-index:3}
.shoe{position:absolute;border-radius:30% 40% 14% 14%}

/* purpose */
.lead{text-align:center}
.panel{left:0;top:658px;width:673px;height:477px;background:var(--teal);border-radius:0 8px 8px 0}
.purpose-item h3{color:var(--white);font-size:23px}
.purpose-item p{color:var(--white);margin-top:14px;width:150px}
.purpose-item .kicker{color:var(--orange);font-size:13px;margin-top:14px}

/* advice cards */
.card{top:1350px;width:203px;height:200px;background:var(--white);border-radius:6px;box-shadow:0 4px 16px rgba(20,40,50,.08);padding:38px 24px}
.card h4{font-size:22px}
.card p{margin-top:12px;font-size:13px}
.card .arrow{margin-top:20px;color:var(--teal)}
.card.featured{top:1320px;height:230px;padding-top:68px;background:linear-gradient(160deg,#1d6579,#0c5367);border-top:6px solid var(--orange)}
.card.featured h4,.card.featured p{color:var(--white)}
.card.featured .arrow{color:var(--orange)}

/* articles */
.post .meta{font-size:10px;letter-spacing:.3px;text-transform:uppercase}
.post h5{font-family:"Barlow Condensed",sans-serif;font-weight:700;font-size:22.5px;line-height:27px;color:var(--ink);margin-top:9px;width:265px}
.post p{margin-top:14px}
.post .kicker{color:var(--teal);margin-top:20px}
.btn{left:159px;top:1971px;width:153px;height:39px;background:var(--orange);color:var(--white);border-radius:3px;display:flex;align-items:center;justify-content:center}

/* footer */
.foot-col h6{font-family:"Barlow Condensed",sans-serif;font-weight:700;font-size:14px;color:var(--ink);text-transform:uppercase}
.foot-col ul{list-style:none;margin-top:14px;font-size:11.5px;line-height:24px}
.foot-social{top:2384px;left:0;width:1200px;display:flex;justify-content:center;gap:50px;font-size:11.5px;text-transform:uppercase}
.foot-social span::before{content:"";display:inline-block;width:10px;height:10px;background:var(--ink);margin-right:8px;vertical-align:-1px}
</style>
</head>
<body>
<div class="page">

<header class="site-header abs">
  <nav class="nav abs" style="left:159px">
    <span>Home</span><span>Info</span><span class="drop">Boots</span><span class="drop">Shoes</span><span class="drop">Gear</span><span class="drop">Footwear</span>
  </nav>
  <div class="brand abs" style="left:0;width:1200px;text-align:center;top:22px">TarnWisp</div>
  <nav class="nav abs" style="left:705px">
    <span class="drop">Sports</span><span>Reviews</span><span>Contact</span>
  </nav>
  <div class="social-dots abs"><i></i><i></i><i></i></div>
</header>

<section class="hero">
  <div class="kicker abs" style="left:158px;top:153px;color:var(--teal);font-size:15px">Welcome to TarnWisp</div>
  <h1 class="display hero-title abs">Where we take<br>outdoor footwear<br>very seriously!</h1>
  <p class="text abs" style="left:158px;top:313px;width:305px">Lorem ipsum dolor sit amet, consectetur adipiscing elit, sed do eiusmod tempor incididunt ut labore et dolore magna aliqua. Ut enim ad minim veniam, quis nostrud exercitation.</p>
  <a class="kicker arrow-link abs" style="left:158px;top:411px;color:var(--teal);font-size:13.5px">Check out a few of our favorites
    <svg class="arrow" viewBox="0 0 12 10"><path d="M0 5h10M6 1l4 4-4 4" fill="none" stroke="currentColor" stroke-width="1.8"/></svg></a>

  <div class="slide abs" style="left:559px;top:162px;width:159px;height:244px;background:linear-gradient(100deg,var(--teal) 0 44%,var(--orange) 44%)">
    <div style="position:absolute;left:0;top:0;width:100%;height:195px;background:var(--teal)"></div>
  </div>
  <div class="shoe" role="img" aria-label="Brown leather hiking boot" style="left:532px;top:232px;width:212px;height:118px;background:linear-gradient(160deg,#4a4035,#2a241e)"></div>
  <div class="slide-label abs" style="left:575px;top:186px;font-size:34px;color:var(--white)">Hiking</div>

  <div class="slide abs" style="left:767px;top:232px;width:113px;height:174px;background:var(--card-grey)"></div>
  <div class="shoe" role="img" aria-label="Black leather combat boot" style="left:760px;top:282px;width:128px;height:92px;background:linear-gradient(160deg,#3a3a3c,#111)"></div>
  <div class="slide-label abs" style="left:778px;top:252px;font-size:19px;color:#7f8488">Combat</div>

  <div class="slide abs" style="left:927px;top:232px;width:113px;height:174px;background:var(--card-grey)"></div>
  <div class="shoe" role="img" aria-label="Brown leather work boot" style="left:918px;top:282px;width:136px;height:90px;background:linear-gradient(160deg,#9a4a2c,#5a2618)"></div>
  <div class="slide-label abs" style="left:939px;top:252px;font-size:19px;color:#7f8488">Work</div>

  <svg class="arrow abs" style="left:1008px;top:416px;color:var(--ink)" viewBox="0 0 12 10"><path d="M12 5H2M6 1L2 5l4 4" fill="none" stroke="currentColor" stroke-width="1.6"/></svg>
  <svg class="arrow abs" style="left:1030px;top:416px;color:var(--teal)" viewBox="0 0 12 10"><path d="M0 5h10M6 1l4 4-4 4" fill="none" stroke="currentColor" stroke-width="1.6"/></svg>
</section>

<section class="purpose">
  <h2 class="display abs" style="left:0;width:1200px;top:529px;text-align:center;font-size:31px">What’s your boot purpose?</h2>
  <p class="text lead abs" style="left:320px;width:560px;top:574px">Sed ut perspiciatis unde omnis iste natus error sit volup tatem accusantium doloremque laudan tium, totam rem aperiam, eaque ipsa quae ab illo inventore veritatis et quas.</p>

  <div class="panel abs"></div>
  <div class="purpose-item abs" style="left:158px;top:718px"><h3 class="display">Walking Shoes</h3><p class="text">Lorem ipsum dolor sit am et, consectetur adipiscing elit, sed do eiusmod tem por incididunt.</p><div class="kicker arrow-link">Learn more <svg class="arrow" viewBox="0 0 12 10"><path d="M0 5h10M6 1l4 4-4 4" fill="none" stroke="currentColor" stroke-width="1.8"/></svg></div></div>
  <div class="purpose-item abs" style="left:373px;top:718px"><h3 class="display">Hiking Gear</h3><p class="text">Lorem ipsum dolor sit am et, consectetur adipiscing elit, sed do eiusmod tem por incididunt.</p><div class="kicker arrow-link">View products <svg class="arrow" viewBox="0 0 12 10"><path d="M0 5h10M6 1l4 4-4 4" fill="none" stroke="currentColor" stroke-width="1.8"/></svg></div></div>
  <div class="purpose-item abs" style="left:158px;top:920px"><h3 class="display">Hunting Boots</h3><p class="text">Lorem ipsum dolor sit am et, consectetur adipiscing elit, sed do eiusmod tem por incididunt.</p><div class="kicker arrow-link">Learn more <svg class="arrow" viewBox="0 0 12 10"><path d="M0 5h10M6 1l4 4-4 4" fill="none" stroke="currentColor" stroke-width="1.8"/></svg></div></div>
  <div class="purpose-item abs" style="left:373px;top:920px"><h3 class="display">Bowling Shoes</h3><p class="text">Lorem ipsum dolor sit am et, consectetur adipiscing elit, sed do eiusmod tem por incididunt.</p><div class="kicker arrow-link">View products <svg class="arrow" viewBox="0 0 12 10"><path d="M0 5h10M6 1l4 4-4 4" fill="none" stroke="currentColor" stroke-width="1.8"/></svg></div></div>

  <div class="abs" role="img" aria-label="Hiker's boots resting on a rocky mountain ledge at sunset" style="left:600px;top:726px;width:442px;height:342px;border-radius:8px;background:linear-gradient(135deg,#5a5560 0%,#8a6e66 35%,#b27a62 55%,#9a9a9e 80%,#3a2f2c 100%)"></div>
</section>

<section class="advice">
  <h2 class="display abs" style="left:0;width:1200px;top:1206px;text-align:center;font-size:31px;line-height:38px">Finally... Shoecare advice<br>that gets results.</h2>
  <div class="card abs" style="left:159px"><h4 class="display">Combat Boots</h4><p class="text">Sed ut perspiciatis unde omnis iste natus error sit volup tatem accusantium doloremque.</p><svg class="arrow" viewBox="0 0 12 10"><path d="M0 5h10M6 1l4 4-4 4" fill="none" stroke="currentColor" stroke-width="1.8"/></svg></div>
  <div class="card featured abs" style="left:386px" role="img" aria-label="Water shoes card over a faded photo of shoes on wet sand"><h4 class="display">Water Shoes</h4><p class="text">Sed ut perspiciatis unde omnis iste natus error sit volup tatem accusantium doloremque.</p><svg class="arrow" viewBox="0 0 12 10"><path d="M0 5h10M6 1l4 4-4 4" fill="none" stroke="currentColor" stroke-width="1.8"/></svg></div>
  <div class="card abs" style="left:611px"><h4 class="display">Nursing Shoes</h4><p class="text">Sed ut perspiciatis unde omnis iste natus error sit volup tatem accusantium doloremque.</p><svg class="arrow" viewBox="0 0 12 10"><path d="M0 5h10M6 1l4 4-4 4" fill="none" stroke="currentColor" stroke-width="1.8"/></svg></div>
  <div class="card abs" style="left:838px"><h4 class="display">Hunting Boots</h4><p class="text">Sed ut perspiciatis unde omnis iste natus error sit volup tatem accusantium doloremque.</p><svg class="arrow" viewBox="0 0 12 10"><path d="M0 5h10M6 1l4 4-4 4" fill="none" stroke="currentColor" stroke-width="1.8"/></svg></div>
</section>

<section class="experts">
  <h2 class="display abs" style="left:157px;top:1645px;font-size:31px;line-height:38px">Learn from<br>the experts</h2>
  <p class="text abs" style="left:158px;top:1736px;width:175px">Sed ut perspiciatis unde om nis iste natus error sit vo lup tatem accusantium dolorem que laudantium, totam rem aperiam, eaque ipsa quae ab illo inventore verita.</p>
  <p class="text abs" style="left:158px;top:1873px;width:175px">Nemo enim ipsam voluptat em quia voluptas sit asperna tur aut odit aut fugit, sed quia consequuntur.</p>
  <div class="btn kicker abs" style="font-size:13.5px">Read reviews</div>

  <article class="post abs" style="left:387px;top:1649px;width:311px">
    <div role="img" aria-label="Hiker with a teal backpack resting on a mountain rock" style="height:162px;border-radius:6px;background:linear-gradient(135deg,#6e8aa0,#c9a45a 40%,#2b6d72 60%,#b9b3a8)"></div>
    <div class="meta" style="margin-top:28px">Features &nbsp;I&nbsp; 3 weeks ago</div>
    <h5>Do My Boots Have The Proper Width For My Feet?</h5>
    <p class="text">If your boots do not have the proper width, you’re gonna have a bad time. If they are too wide, you will not have enough support.</p>
    <div class="kicker arrow-link">Read more <svg class="arrow" viewBox="0 0 12 10"><path d="M0 5h10M6 1l4 4-4 4" fill="none" stroke="currentColor" stroke-width="1.8"/></svg></div>
  </article>
  <article class="post abs" style="left:730px;top:1649px;width:311px">
    <div role="img" aria-label="Person in brown boots with a leather bag beside a shuttered wall" style="height:162px;border-radius:6px;background:linear-gradient(90deg,#4a3a30,#9a9c9e 45%,#d2d4d6 80%,#8a8c8e)"></div>
    <div class="meta" style="margin-top:28px">Features &nbsp;I&nbsp; 3 weeks ago</div>
    <h5>How To Buy The Right Boots For Your Personal Situation</h5>
    <p class="text">If you are in the process of buying a new pair of boots, you would want to see to it that the one you do end up with is the best that you can find.</p>
    <div class="kicker arrow-link">Read more <svg class="arrow" viewBox="0 0 12 10"><path d="M0 5h10M6 1l4 4-4 4" fill="none" stroke="currentColor" stroke-width="1.8"/></svg></div>
  </article>
</section>

<footer class="site-footer">
  <div class="brand abs" style="left:158px;top:2166px">TarnWisp</div>
  <div class="foot-col abs" style="left:366px;top:2170px"><h6>About</h6><ul><li>About</li><li>Contact</li><li>Media</li></ul></div>
  <div class="foot-col abs" style="left:496px;top:2170px"><h6>Company</h6><ul><li>Terms of Use</li><li>Privacy Policy</li><li>Editorial Policy</li><li>How We Make Money</li></ul></div>
  <div class="foot-col abs" style="left:683px;top:2170px"><h6>Discover</h6><ul><li>Products</li><li>Skin Type</li><li>Skin Concerns</li><li>Reviews</li></ul></div>
  <div class="foot-col abs" style="left:825px;top:2170px;width:218px"><h6>How we make money</h6><p style="margin-top:18px;font-size:10.5px;line-height:15px">Lorem ipsum dolor sit amet, consectetur adipiscing elit, sed do eiusmod tempor incidi dunt ut labore et dolore magna aliqua. Ut enim ad minim veniam, quis nostrud exer citation ullamco laboris nisi ut.</p></div>
  <div class="abs" style="left:158px;top:2357px;width:885px;height:1px;background:#c5cfd4"></div>
  <div class="foot-social abs"><span>Chirpline</span><span>Snapframe</span><span>Friendwall</span></div>
  <div class="abs" style="left:0;width:1200px;top:2426px;text-align:center;font-size:10.5px">© Copyright 2021 TarnWisp. All rights reserved.</div>
</footer>

</div>
</body>
</html>
```